Brivolt VoIP COMMERCIAL PHONE FLYER

We are a full service telecom VoIP company that offers local, long distance calling plans to business clients. We offer local installations, and local service we have a hands on approach and will match or beat any competitor. We work with all types of business. We are fully HIPPA complient in the medical field

Target Market(s)

SMALL TO MEDIUM BUSINESS, Medical, Real Estate, Lawyer, Accounting

Industry/Entity Type

VoIP

Font styles to use
Serif

Colors
0054AA
0677BA
7BADD7
CADEEF
E8F1F8

Requirements
Must have
• Modern/ Current picture of phone reader friendly
Nice to have
• free flow, friendly, modern
Should not have
• stuffy, corporate feel

```html
<!DOCTYPE html>
<html lang="en">
<head>
<meta charset="utf-8">
<title>Brivolt VoIP – Free Telephone Lines Flyer</title>
<link rel="stylesheet" href="https://fonts.googleapis.com/css2?family=Josefin+Sans:wght@400;600&family=Montserrat:wght@500;700;800;900&family=Roboto:wght@400;500&display=swap">
<style>
  :root {
    --blue-deep: #0054AA;
    --blue-mid: #0677BA;
    --blue-light: #7BADD7;
    --blue-pale: #CADEEF;
    --blue-mist: #E8F1F8;
    --ink: #1b1b1b;
    --footer: #3d3d3f;
    --white: #ffffff;
    --muted: #555a60;
  }
  * { box-sizing: border-box; margin: 0; padding: 0; }
  html, body { width: 800px; height: 1200px; overflow: hidden; background: var(--white); }
  .flyer { position: relative; width: 800px; height: 1200px; overflow: hidden; background: var(--white); font-family: "Montserrat", sans-serif; }
  .abs { position: absolute; }
  .hero-art { position: absolute; left: 0; top: 0; }

  .brand { left: 30px; top: 44px; display: flex; align-items: center; gap: 12px; }
  .brand-mark { width: 30px; height: 30px; background: var(--blue-mid); }
  .brand-name { font-family: "Montserrat", sans-serif; font-weight: 800; font-size: 44px; color: var(--blue-mid); letter-spacing: 1px; line-height: 1; }

  .headline { left: 24px; top: 150px; color: var(--ink); font-family: "Josefin Sans", sans-serif; line-height: 1; }
  .headline .line-sm { font-size: 43px; display: block; margin-bottom: 6px; }
  .headline .line-key { font-family: "Montserrat", sans-serif; font-weight: 900; font-size: 52px; color: var(--blue-mid); display: block; margin-bottom: 4px; letter-spacing: -0.5px; }
  .headline .line-lg { font-size: 60px; display: block; }

  .tagline-band { left: 0; top: 414px; width: 540px; height: 58px; background: var(--blue-mid); }
  .tagline { left: 27px; top: 424px; font-weight: 800; font-size: 31px; color: var(--white); }

  .savings-band { left: 0; top: 535px; width: 800px; height: 230px; background: linear-gradient(90deg, var(--blue-deep), var(--blue-mid) 60%, var(--blue-deep)); }
  .savings { left: 40px; top: 560px; width: 320px; text-align: center; color: var(--white); }
  .savings .kicker { font-weight: 900; font-size: 38px; letter-spacing: 1px; }
  .savings .figure { font-weight: 900; font-size: 92px; line-height: 1; color: var(--blue-pale); }
  .savings .sub { font-weight: 700; font-size: 22px; margin-top: 6px; white-space: nowrap; }

  .phone-art { left: 395px; top: 488px; }

  .why-title { left: 30px; top: 812px; font-weight: 900; font-size: 34px; color: var(--blue-deep); }
  .feature { top: 898px; display: flex; gap: 12px; }
  .feature-icon { width: 63px; height: 70px; background: linear-gradient(180deg, var(--blue-mid), var(--blue-deep)); display: flex; align-items: center; justify-content: center; flex: none; }
  .feature h3 { font-weight: 800; font-size: 16.5px; color: var(--blue-deep); margin-top: 10px; }
  .feature p { font-family: "Roboto", sans-serif; font-size: 8.6px; color: var(--muted); line-height: 1.35; margin-top: 10px; }
  .feature.f1 { left: 30px; width: 250px; }
  .feature.f2 { left: 296px; width: 230px; }
  .feature.f3 { left: 540px; width: 230px; }

  .footer { left: 0; top: 1048px; width: 800px; height: 152px; background: var(--footer); }
  .cta { left: 148px; top: 1025px; width: 487px; height: 46px; border-radius: 8px; background: var(--blue-deep); color: var(--white); font-weight: 700; font-size: 21px; display: flex; align-items: center; justify-content: center; }

  .call { left: 22px; top: 1103px; width: 244px; height: 52px; }
  .call-pill { position: absolute; left: 26px; top: 7px; width: 218px; height: 38px; border: 1.5px solid var(--white); border-radius: 0 20px 20px 0; border-left: none; }
  .call-badge { position: absolute; left: 0; top: 0; width: 52px; height: 52px; border-radius: 50%; background: var(--white); display: flex; align-items: center; justify-content: center; }
  .call-number { position: absolute; left: 70px; top: 12px; font-family: "Josefin Sans", sans-serif; font-weight: 600; font-size: 23px; color: var(--white); }

  .contact { left: 338px; top: 1102px; color: var(--white); font-family: "Roboto", sans-serif; }
  .contact-row { display: flex; align-items: flex-start; gap: 12px; }
  .contact-row + .contact-row { margin-top: 10px; align-items: center; }
  .address { font-size: 11px; line-height: 1.25; }
  .email { font-size: 14px; }

  .social { left: 628px; top: 1112px; width: 150px; display: flex; justify-content: center; gap: 14px; }
  .social span { width: 13px; height: 13px; border-radius: 50%; background: var(--white); }
  .web { left: 628px; top: 1140px; width: 150px; text-align: center; color: var(--white); font-family: "Roboto", sans-serif; font-size: 13px; }
</style>
</head>
<body>
<main class="flyer">

  <svg class="hero-art" width="800" height="490" viewBox="0 0 800 490" aria-hidden="false">
    <polygon points="305,0 800,0 800,28 352,28 500,405 468,405" fill="var(--blue-mid)"/>
    <defs>
      <linearGradient id="officeTone" x1="0" y1="0" x2="1" y2="1">
        <stop offset="0" stop-color="#a9bccd"/>
        <stop offset="0.5" stop-color="#6f8fae"/>
        <stop offset="1" stop-color="#c9b39a"/>
      </linearGradient>
    </defs>
    <polygon role="img" aria-label="Photo of a person dialling a desk telephone in an office" points="352,28 800,28 800,482 540,482 505,405" fill="url(#officeTone)"/>
  </svg>

  <div class="abs brand">
    <span class="brand-mark"></span>
    <span class="brand-name">Brivolt</span>
  </div>

  <h1 class="abs headline">
    <span class="line-sm">WE OFFER FREE</span>
    <span class="line-key">TELEPHONE</span>
    <span class="line-sm">LINES FOR YOUR</span>
    <span class="line-lg">BUSINESS</span>
  </h1>

  <div class="abs tagline-band"></div>
  <p class="abs tagline">Your Business on The Cloud</p>

  <div class="abs savings-band"></div>
  <div class="abs savings">
    <p class="kicker">SAVE OVER</p>
    <p class="figure">35%</p>
    <p class="sub">On Your Monthly Phone Bills</p>
  </div>

  <svg class="abs phone-art" width="365" height="385" viewBox="0 0 365 385">
    <defs>
      <linearGradient id="deviceTone" x1="0" y1="0" x2="1" y2="1">
        <stop offset="0" stop-color="#4a4d52"/>
        <stop offset="0.55" stop-color="#2a2c30"/>
        <stop offset="1" stop-color="#55585d"/>
      </linearGradient>
    </defs>
    <path role="img" aria-label="Modern video desk phone with touchscreen and corded handset" d="M40,10 L290,40 Q330,45 335,90 L360,300 Q362,330 335,330 L20,250 Q0,245 5,220 L25,30 Q28,8 40,10 Z" fill="url(#deviceTone)"/>
  </svg>

  <h2 class="abs why-title">WHY CHOOSE US?</h2>

  <div class="abs feature f1">
    <div class="feature-icon">
      <svg width="36" height="40" viewBox="0 0 36 40" fill="none" stroke="#fff" stroke-width="2.4" stroke-linecap="round">
        <path d="M18 10a9 9 0 0 0-5 16.5V30h10v-3.5A9 9 0 0 0 18 10z" fill="#fff"/>
        <path d="M14 34h8M15 37h6M18 1v4M4 7l3 3M32 7l-3 3M1 19h4M31 19h4"/>
      </svg>
    </div>
    <div>
      <h3>Powerful Features</h3>
      <p>Lorem ipsum dolor sit amet, consectetur adipiscing elit, sed do eiusmod tempor incididunt ut labore.</p>
    </div>
  </div>

  <div class="abs feature f2">
    <div class="feature-icon">
      <svg width="36" height="40" viewBox="0 0 36 40" fill="none" stroke="#fff" stroke-width="2.4" stroke-linecap="round">
        <path d="M15 14v14l-4-3-3 3 8 10h12l3-12-11-3v-9a2.5 2.5 0 0 0-5 0z" fill="#fff"/>
        <path d="M10 4l3 4M17 1v5M24 4l-3 4"/>
      </svg>
    </div>
    <div>
      <h3>Easy To Use</h3>
      <p>Lorem ipsum dolor sit amet, consectetur adipiscing elit, sed do eiusmod tempor.</p>
    </div>
  </div>

  <div class="abs feature f3">
    <div class="feature-icon">
      <svg width="40" height="40" viewBox="0 0 40 40" fill="none" stroke="#fff" stroke-width="2.6" stroke-linecap="round">
        <circle cx="17" cy="17" r="9"/>
        <circle cx="17" cy="17" r="3.5"/>
        <path d="M17 3v4M17 27v4M3 17h4M27 17h4M7 7l3 3M24 24l3 3M27 7l-3 3M7 27l3-3"/>
        <path d="M24 24l10 10"/>
      </svg>
    </div>
    <div>
      <h3>Easy Set Up</h3>
      <p>Lorem ipsum dolor sit amet, consectetur adipiscing elit.</p>
    </div>
  </div>

  <div class="abs footer"></div>
  <div class="abs cta">CALL TODAY FOR YOUR FREE PHONES!</div>

  <div class="abs call">
    <div class="call-pill"></div>
    <div class="call-badge">
      <svg width="24" height="24" viewBox="0 0 24 24">
        <path d="M6.6 10.8a15.2 15.2 0 0 0 6.6 6.6l2.2-2.2a1 1 0 0 1 1-.25 11.4 11.4 0 0 0 3.6.6 1 1 0 0 1 1 1V20a1 1 0 0 1-1 1A17 17 0 0 1 3 4a1 1 0 0 1 1-1h3.5a1 1 0 0 1 1 1c0 1.25.2 2.45.6 3.6a1 1 0 0 1-.25 1z" fill="var(--blue-mid)"/>
      </svg>
    </div>
    <span class="call-number">555-014-2290</span>
  </div>

  <div class="abs contact">
    <div class="contact-row">
      <svg width="12" height="17" viewBox="0 0 12 17"><path d="M6 0a6 6 0 0 0-6 6c0 4.5 6 11 6 11s6-6.5 6-11a6 6 0 0 0-6-6zm0 8.2A2.2 2.2 0 1 1 6 3.8a2.2 2.2 0 0 1 0 4.4z" fill="var(--blue-light)"/></svg>
      <p class="address">18 Harbor Lane, Eastfield,<br>Eastfield- 100482</p>
    </div>
    <div class="contact-row">
      <svg width="16" height="14" viewBox="0 0 16 14" fill="none" stroke="var(--blue-light)" stroke-width="1.4"><rect x="1" y="1" width="14" height="12" rx="1"/><path d="M1 2l7 6 7-6"/></svg>
      <p class="email">hello@brivolt.example</p>
    </div>
  </div>

  <div class="abs social" aria-hidden="true"><span></span><span></span><span></span></div>
  <p class="abs web">www.brivolt.example</p>

</main>
</body>
</html>
```